Business Card Design EFTPOS Comparison site

At QuoteHarbor.com.au we are a free service that allows our customers to get up to five quotes from our panel of suppliers for a range of BUSINESS related products and services. These products include eftpos / credit card machines, bank accounts, insurance, signage,office furniture etc. basically anything that a small business would need.
The process is done in 3 steps; 1) register your enquiry 2) we source and provide the five cheapest quotes 3) then select the supplier of your choice,the process is simple ABC and is FREE.
Please visit the soon to be revamped website to see our logo.
Target Market(s)
Small business operators
Industry/Entity Type
Small Business
Requirements
Must have
- Double Sided card

```html
<!DOCTYPE html>
<html lang="en">
<head>
<meta charset="utf-8">
<title>QuoteHarbor Business Card</title>
<link rel="stylesheet" href="https://fonts.googleapis.com/css2?family=Arimo:wght@400;700&display=swap">
<style>
  :root {
    --stage: #1e1e1e;
    --card-front: #f7f7f7;
    --card-front-edge: #e4e4e4;
    --card-back: #2b2a29;
    --accent: #f0a11c;
    --ink-light: #f2f2f2;
    --brand: #e8891c;
  }
  * { box-sizing: border-box; margin: 0; padding: 0; }
  html, body {
    width: 1200px;
    height: 900px;
    overflow: hidden;
    background: var(--stage);
    font-family: "Arimo", Arial, sans-serif;
  }
  .canvas {
    position: relative;
    width: 1200px;
    height: 900px;
  }
  .card {
    position: absolute;
    width: 560px;
    height: 320px;
    box-shadow: 0 14px 30px rgba(0,0,0,0.55);
  }
  .card-front {
    left: 90px;
    top: 110px;
    background: radial-gradient(ellipse at 50% 45%, #ffffff 0%, var(--card-front) 55%, var(--card-front-edge) 100%);
    display: flex;
    align-items: center;
    justify-content: center;
  }
  .brand {
    display: flex;
    align-items: center;
    gap: 14px;
  }
  .brand-dot {
    width: 34px;
    height: 34px;
    border-radius: 50%;
    background: var(--brand);
  }
  .brand-name {
    font-weight: 700;
    font-size: 46px;
    color: var(--brand);
    letter-spacing: -0.5px;
  }
  .card-back {
    left: 560px;
    top: 480px;
    background: var(--card-back);
  }
  .identity {
    position: absolute;
    right: 300px;
    top: 150px;
    text-align: left;
  }
  .identity-name {
    font-weight: 700;
    font-size: 24px;
    color: var(--ink-light);
    letter-spacing: 0.5px;
    line-height: 1;
  }
  .identity-name .initial { color: var(--accent); }
  .identity-role {
    font-weight: 700;
    font-size: 18px;
    color: var(--ink-light);
    margin-top: 4px;
  }
  .divider {
    position: absolute;
    left: 280px;
    top: 110px;
    width: 2px;
    height: 110px;
    background: var(--accent);
  }
  .contacts {
    position: absolute;
    left: 296px;
    top: 118px;
    list-style: none;
  }
  .contacts li {
    display: flex;
    align-items: center;
    gap: 8px;
    font-size: 14px;
    color: var(--ink-light);
    height: 22px;
  }
  .contacts svg { width: 13px; height: 13px; flex: none; }
</style>
</head>
<body>
<main class="canvas">
  <section class="card card-front" aria-label="Card front">
    <div class="brand">
      <span class="brand-dot"></span>
      <span class="brand-name">QuoteHarbor</span>
    </div>
  </section>

  <section class="card card-back" aria-label="Card back">
    <div class="identity">
      <p class="identity-name"><span class="initial">Y</span>OUR <span class="initial">N</span>AME</p>
      <p class="identity-role">Company Position</p>
    </div>
    <div class="divider"></div>
    <ul class="contacts">
      <li>
        <svg viewBox="0 0 16 16" aria-hidden="true"><circle cx="8" cy="8" r="7" fill="none" stroke="var(--accent)" stroke-width="1.5"/><path d="M5 4.5l2 2-1 1.2c.6 1.2 1.4 2 2.5 2.5l1.2-1 2 2-1.2 1.2C7.6 12 4.2 8.6 4 5.7z" fill="var(--accent)"/></svg>
        000 123 4567
      </li>
      <li>
        <svg viewBox="0 0 16 16" aria-hidden="true"><path d="M8 1.5L1 8h2v6.5h4V10h2v4.5h4V8h2z" fill="var(--accent)"/></svg>
        your address
      </li>
      <li>
        <svg viewBox="0 0 16 16" aria-hidden="true"><rect x="1" y="3.5" width="14" height="9" rx="1" fill="none" stroke="var(--accent)" stroke-width="1.5"/><path d="M1.5 4l6.5 5 6.5-5" fill="none" stroke="var(--accent)" stroke-width="1.5"/></svg>
        youremail@domain.com
      </li>
      <li>
        <svg viewBox="0 0 16 16" aria-hidden="true"><path d="M8 1a4.5 4.5 0 0 0-4.5 4.5C3.5 9 8 15 8 15s4.5-6 4.5-9.5A4.5 4.5 0 0 0 8 1zm0 6.3a1.8 1.8 0 1 1 0-3.6 1.8 1.8 0 0 1 0 3.6z" fill="var(--accent)"/></svg>
        QuoteHarbor.com.au
      </li>
    </ul>
  </section>
</main>
</body>
</html>
```